Dryer Vent Cleaning Postcard Design

We need a postcard design for Duct Rangers, a company that specializes in dryer vent cleaning, repairs and upgrades. Dryer vents need periodic cleaning to avoid lint clogging, dryer malfunction, long dry times and even a house fire. This card will be sent to residential and businesses prospects to introduce them to our services and the importance of maintaining their dryer vents. Our website is @ ductranging.example and provides information about our services, photos of our work and our general color scheme (purple/orange). Final print size will be 5x7 horizontal.

Target Market(s)

homeowners and business owners (spas, salons, grooming, gyms, laundrymats, etc)

Requirements
Must have
• Reduce the risk of fire
shortened dry times
lower energy consumption
18000 dryer fires caused in the US per year
Nice to have
• Does your dryer take too long to dry?

```html
<!DOCTYPE html>
<html lang="en">
<head>
<meta charset="utf-8">
<title>Duct Rangers – Dryer Vent Cleaning Postcard</title>
<link href="https://fonts.googleapis.com/css2?family=Fira+Sans:ital,wght@0,300;0,400;0,600;0,700;1,700&family=Dosis:wght@400&family=Roboto+Condensed:ital,wght@1,700&display=swap" rel="stylesheet">
<style>
  :root {
    --board: #a87d55;
    --paper: #ffffff;
    --purple: #433a73;
    --purple-band: #4d3f80;
    --orange: #f07f3c;
    --red: #e8432c;
    --sky: #6f93d6;
    --soft-blue: #7aa0dc;
    --grey-line: #b9b9bd;
    --ink: #2b2b33;
    --ring: #fcd869;
  }
  * { box-sizing: border-box; margin: 0; padding: 0; }
  html, body { width: 878px; height: 1200px; overflow: hidden; }
  body { background: var(--board); position: relative; font-family: "Fira Sans", sans-serif; }

  .postcard {
    position: absolute; left: 145px; width: 577px; height: 447px;
    background: var(--paper); overflow: hidden;
    box-shadow: 4px 5px 8px rgba(0,0,0,.35);
  }
  .postcard--front { top: 140px; }
  .postcard--back { top: 609px; left: 142px; height: 446px;
    background: linear-gradient(160deg, #ffffff 0%, #f1f1f3 45%, #ffffff 70%, #ededf0 100%); }

  .layer { position: absolute; inset: 0; width: 100%; height: 100%; }

  /* front */
  .headline { position: absolute; left: 31px; top: 20px; color: var(--purple);
    font-weight: 700; font-size: 33px; line-height: 39px; letter-spacing: -.2px; }
  .guarantee { position: absolute; left: 31px; top: 111px; color: var(--red);
    font-weight: 700; font-size: 17px; }
  .service-area { position: absolute; left: 31px; top: 139px; width: 320px;
    color: var(--sky); font-weight: 400; font-size: 12.5px; line-height: 17.5px; }
  .benefits { position: absolute; left: 31px; top: 187px; list-style: none;
    font-family: "Dosis", sans-serif; font-size: 14px; color: var(--ink); }
  .benefits li { position: relative; padding-left: 19px; line-height: 20.5px; }
  .benefits li::before { content: ""; position: absolute; left: 0; top: 5px;
    width: 12px; height: 12px; border-radius: 50%;
    background: radial-gradient(circle at 35% 35%, #7fc2f5, #1b63b7); }
  .benefits .wrap { line-height: 18px; }

  .brand-mark { position: absolute; display: flex; align-items: center; gap: 8px; }
  .brand-mark .dot { width: 22px; height: 22px; border-radius: 50%; background: var(--orange); }
  .brand-mark .name { color: var(--purple); font-weight: 700; font-size: 24px; white-space: nowrap; }
  .postcard--front .brand-mark { left: 385px; top: 140px; }
  .postcard--back .brand-mark { left: 30px; top: 75px; }
  .postcard--back .brand-mark .name { font-size: 22px; }

  .laundry-photo { position: absolute; left: 175px; top: 202px; width: 246px; height: 246px;
    border-radius: 50%; border: 5px solid var(--ring);
    background: radial-gradient(circle at 60% 40%, #f4f1ee 0%, #ddd7d2 45%, #9fbf5c 75%, #c9c4c0 100%); }

  .front-contact { position: absolute; left: 33px; top: 380px;
    font-family: "Roboto Condensed", sans-serif; font-style: italic; font-weight: 700; }
  .front-contact .phone { color: #fff; font-size: 25px; line-height: 28px; display: block; }
  .front-contact .site { color: var(--orange); font-size: 21px; line-height: 28px; display: block; }

  /* back */
  .divider { position: absolute; left: 214px; top: 22px; width: 1px; height: 295px; background: #cfcfd4; }
  .question { position: absolute; left: 14px; width: 180px; top: 175px; text-align: center;
    color: var(--purple); font-weight: 700; font-size: 19px; line-height: 22px; }
  .invite { position: absolute; left: 14px; width: 180px; top: 259px; text-align: center;
    color: var(--purple); font-weight: 300; font-size: 13px; line-height: 16.5px; }
  .call-today { position: absolute; left: 14px; width: 180px; top: 349px; text-align: center;
    color: var(--red); font-weight: 400; font-size: 15px; }
  .back-phone { position: absolute; left: 14px; width: 180px; top: 369px; text-align: center;
    color: var(--purple); font-weight: 700; font-size: 21px; }

  .service-title { position: absolute; left: 235px; top: 18px; color: var(--red);
    font-weight: 700; font-style: italic; font-size: 19.5px; }
  .service-copy { position: absolute; left: 235px; top: 50px; width: 320px;
    color: var(--purple); font-size: 12.4px; line-height: 15.8px; }

  .before-after { position: absolute; left: 235px; width: 106px; height: 80px;
    border: 1.5px solid #c0683b;
    background: linear-gradient(90deg, #8c8c8c 0%, #5e5e5e 49%, #fff 49.5%, #fff 50.5%, #4a4a4a 51%, #9a9a9a 100%); }
  .before-after--one { top: 126px; }
  .before-after--two { top: 213px; }

  .technician-art { position: absolute; left: 372px; top: 115px; width: 180px; height: 210px;
    border-radius: 6px; background: linear-gradient(180deg, #e9e4f1 0%, #c9b8a8 55%, #d8dbf0 100%); }
  .email { position: absolute; left: 235px; top: 303px; display: flex; align-items: center; gap: 5px;
    color: var(--ink); font-weight: 600; font-size: 12px; }

  .cleaning-art { position: absolute; left: 205px; top: 338px; width: 342px; height: 82px;
    border-radius: 6px; background: linear-gradient(90deg, #e8d3c2 0%, #e6e6ea 55%, #cfd0d6 100%); }
</style>
</head>
<body>

<section class="postcard postcard--front">
  <svg class="layer" viewBox="0 0 577 447" aria-hidden="true">
    <path d="M0 303 C120 292 220 325 310 362" fill="none" stroke="var(--grey-line)" stroke-width="4"/>
    <path d="M577 238 C540 330 470 395 390 410" fill="none" stroke="var(--grey-line)" stroke-width="4"/>
    <path d="M0 310 C130 300 250 360 330 395 C420 430 520 380 577 250 L577 447 L0 447 Z" fill="var(--orange)"/>
  </svg>

  <h1 class="headline">Damp Clothes? Long dry times?<br>Get your vents cleaned!</h1>
  <p class="guarantee">Our work is Guaranteed and Fully Insured</p>
  <p class="service-area">Dryer vent cleaning in Greensboro NC, Summerfield, High Point, Winston Salem &amp; surrounding areas!</p>
  <ul class="benefits">
    <li>Reduce the risk of fire</li>
    <li>Shortened dry times</li>
    <li>Lower energy consumption</li>
    <li class="wrap">18000 dryer fires caused in<br>the us per year</li>
  </ul>

  <div class="brand-mark"><span class="dot"></span><span class="name">Duct Rangers</span></div>

  <div class="laundry-photo" role="img" aria-label="Photo of a smiling woman folding a green towel beside a washing machine"></div>

  <svg class="layer" viewBox="0 0 577 447" aria-hidden="true">
    <path d="M0 358 C130 338 250 378 340 408 C430 438 520 408 577 318 L577 447 L0 447 Z" fill="var(--red)"/>
    <path d="M0 370 C130 350 260 400 360 425 C450 445 530 420 577 355 L577 447 L0 447 Z" fill="var(--purple-band)"/>
  </svg>

  <div class="front-contact">
    <span class="phone">555-010-8001</span>
    <span class="site">DuctRanging.example</span>
  </div>
</section>

<section class="postcard postcard--back">
  <div class="brand-mark"><span class="dot"></span><span class="name">Duct Rangers</span></div>

  <h2 class="question">Does your<br>dryer take too<br>long to dry?</h2>
  <p class="invite">Feel free to give us a call or contact us through our online form or schedule your appointment online!</p>
  <p class="call-today">Call Today!</p>
  <p class="back-phone">555-010-6045</p>

  <div class="divider"></div>

  <h2 class="service-title">Dryer Vent Repair &amp; Installation</h2>
  <p class="service-copy">We specializes in dryer vent cleaning, repairs and upgrades. Dryer vents need periodic cleaning to avoid lint clogging, dryer malfunction, long dry times and even a house fire.</p>

  <div class="before-after before-after--one" role="img" aria-label="Before and after photos of a lint-clogged dryer duct"></div>
  <div class="before-after before-after--two" role="img" aria-label="Before and after photos of a cleaned dryer vent"></div>

  <div class="technician-art" role="img" aria-label="Illustration of a vent technician holding a duct brush with a hose backpack"></div>

  <p class="email">
    <svg width="16" height="11" viewBox="0 0 16 11" aria-hidden="true">
      <rect width="16" height="11" fill="var(--red)"/>
      <path d="M0 0 L8 6 L16 0" fill="none" stroke="#fff" stroke-width="1.3"/>
    </svg>
    office@ductranging.example
  </p>

  <div class="cleaning-art" role="img" aria-label="Illustration of a technician pushing a brush through a duct toward a dryer"></div>

  <svg class="layer" viewBox="0 0 577 446" aria-hidden="true">
    <path d="M0 385 Q300 445 577 388 L577 446 L0 446 Z" fill="var(--soft-blue)"/>
    <path d="M0 400 Q300 455 577 397 L577 446 L0 446 Z" fill="var(--red)"/>
    <path d="M0 406 Q300 462 577 404 L577 446 L0 446 Z" fill="var(--purple-band)"/>
  </svg>
</section>

</body>
</html>
```